Business cards and logo for kitchen and bath remodeling company

We want an elegant card but that calls attention something unique and when people see it they remember us. A log that we can use for our own. We are a kitchen and bathroom remodeling company. We are 3 partners staring the company we are located in seattle washington usa. We try to give the best experience and luxury look in our projects and we are looking to show that in our cards. I added a sample of a card I really like. I like the black and gold look but gray blue or green in a metallic look would look nice. I'm open to any color.

Target Market(s)

Home owners.

Industry/Entity Type

Construction

Contact Information for Business Card

Copperfern builders

Colors

Designer to choose colors to be used in the design.

Requirements
Must have
• Make a Logo
• Logo to be unique
• Name of company copperfern builders
Nice to have
• Have a good color scheme
• Front design to connect with back of card

```html
<!DOCTYPE html>
<html lang="en">
<head>
<meta charset="utf-8">
<title>Copperfern Builders – Business Card</title>
<link rel="stylesheet" href="https://fonts.googleapis.com/css2?family=Lato:wght@400;700&family=Montserrat:wght@800&display=swap">
<style>
  :root {
    --page-bg: #e9eaee;
    --brand-blue: #3a55a6;
    --card-white: #ffffff;
    --ink: #1f1f24;
    --card-shadow: 0 10px 28px rgba(20, 24, 40, 0.22);
  }
  * { box-sizing: border-box; margin: 0; padding: 0; }
  html, body {
    width: 1200px; height: 900px; overflow: hidden;
    background: var(--page-bg);
    font-family: "Lato", sans-serif;
  }
  .sheet {
    width: 1200px; height: 900px;
    display: flex; flex-direction: column;
    align-items: center; justify-content: center; gap: 40px;
  }
  .card {
    width: 700px; height: 400px;
    border-radius: 22px;
    box-shadow: var(--card-shadow);
    position: relative;
    overflow: hidden;
  }
  .card--back { background: var(--brand-blue); display: flex; align-items: center; justify-content: center; }
  .card--front { background: var(--card-white); display: flex; align-items: center; }

  .wordmark { display: flex; flex-direction: column; align-items: center; gap: 14px; }
  .wordmark__square { width: 70px; height: 70px; border: 2px solid currentColor; }
  .wordmark__name {
    font-family: "Lato", sans-serif; font-weight: 400;
    font-size: 40px; letter-spacing: 0.5px; line-height: 1;
  }
  .card--back .wordmark { color: var(--card-white); }
  .card--front .wordmark { color: var(--brand-blue); }
  .card--front .wordmark__name { font-size: 32px; }
  .card--front .wordmark__square { width: 58px; height: 58px; }

  .front__logo { width: 355px; display: flex; justify-content: center; padding-left: 20px; }
  .front__divider { width: 1.5px; height: 170px; background: var(--brand-blue); }
  .front__details { padding-left: 34px; }

  .person__name {
    font-family: "Montserrat", sans-serif; font-weight: 800;
    font-size: 33px; color: var(--brand-blue); line-height: 1.05;
  }
  .person__title { font-size: 19px; color: var(--ink); margin-top: 4px; }

  .contact { list-style: none; margin-top: 18px; display: flex; flex-direction: column; gap: 8px; }
  .contact__item { display: flex; align-items: center; gap: 12px; font-size: 17px; color: var(--ink); }
  .contact__icon { width: 18px; height: 18px; flex: none; color: var(--brand-blue); }
  .contact__accent { color: var(--brand-blue); }
</style>
</head>
<body>
<main class="sheet">
  <section class="card card--back" aria-label="Card back">
    <div class="wordmark">
      <span class="wordmark__square"></span>
      <span class="wordmark__name">Copperfern builders</span>
    </div>
  </section>

  <section class="card card--front" aria-label="Card front">
    <div class="front__logo">
      <div class="wordmark">
        <span class="wordmark__square"></span>
        <span class="wordmark__name">Copperfern builders</span>
      </div>
    </div>
    <div class="front__divider"></div>
    <div class="front__details">
      <h1 class="person__name">Marisol Averett</h1>
      <p class="person__title">Founder &amp; CEO</p>
      <ul class="contact">
        <li class="contact__item">
          <svg class="contact__icon" viewBox="0 0 24 24" fill="currentColor" aria-hidden="true"><path d="M6.6 10.8a15.1 15.1 0 0 0 6.6 6.6l2.2-2.2c.3-.3.7-.4 1-.2 1.1.4 2.3.6 3.6.6.6 0 1 .4 1 1V20c0 .6-.4 1-1 1A17 17 0 0 1 3 4c0-.6.4-1 1-1h3.5c.6 0 1 .4 1 1 0 1.3.2 2.5.6 3.6.1.3 0 .7-.2 1z"/></svg>
          <span>206 555 0147</span>
        </li>
        <li class="contact__item">
          <svg class="contact__icon" viewBox="0 0 24 24" fill="currentColor" aria-hidden="true"><path d="M2 5h20v14H2z M3.5 6.5 12 13l8.5-6.5" stroke="#fff" stroke-width="1.4"/></svg>
          <span>hello@copperfernmail.com</span>
        </li>
        <li class="contact__item">
          <svg class="contact__icon" viewBox="0 0 24 24" fill="none" stroke="currentColor" stroke-width="1.8" aria-hidden="true"><circle cx="12" cy="12" r="9.5"/><ellipse cx="12" cy="12" rx="4" ry="9.5"/><path d="M2.5 12h19M4 7h16M4 17h16"/></svg>
          <span>www.<span class="contact__accent">copperfernbuilders</span>.com</span>
        </li>
      </ul>
    </div>
  </section>
</main>
</body>
</html>
```